Looking for something outstanding

2 side business card, one side just the logo preferably the metallic 3D color or my original logo for uv printing. Be creative

Colors

Designer to choose colors to be used in the design.

Requirements
Must have
• Here my info for the business cards
• Owen Hardy
• President
• (555) 302-8816
• Owen@cobaltbuildgroup.com
• Office@cobaltbuildgroup.com
• www.cobaltbuildgroup.com
• FB @cobaltbuildgroup
• Dallas-Fort Worth

```html
<!DOCTYPE html>
<html lang="en">
<head>
<meta charset="utf-8">
<title>Cobalt Build Group – Business Card Front</title>
<link href="https://fonts.googleapis.com/css2?family=Montserrat:wght@500&display=swap" rel="stylesheet">
<style>
  :root {
    --card-base: #0b121a;
    --band-deep: #121c28;
    --band-mid: #1a2636;
    --band-blue: #243552;
    --band-steel: #3e5468;
    --logo-ink: #e2e6e8;
  }
  html, body {
    margin: 0;
    padding: 0;
    width: 1200px;
    height: 710px;
    overflow: hidden;
    background: var(--card-base);
  }
  .card {
    position: relative;
    width: 1200px;
    height: 710px;
    overflow: hidden;
    background: var(--card-base);
  }
  .card-bands {
    position: absolute;
    inset: 0;
    width: 1200px;
    height: 710px;
  }
  .brand-lockup {
    position: absolute;
    left: 160px;
    top: 262px;
    display: flex;
    align-items: center;
    gap: 34px;
  }
  .brand-square {
    width: 150px;
    height: 150px;
    background: var(--logo-ink);
    flex: none;
  }
  .brand-name {
    font-family: "Montserrat", sans-serif;
    font-weight: 500;
    color: var(--logo-ink);
    line-height: 1;
    margin: 0;
  }
  .brand-name .brand-primary {
    display: block;
    font-size: 112px;
    letter-spacing: 0.12em;
  }
  .brand-name .brand-secondary {
    display: block;
    font-size: 40px;
    letter-spacing: 0.36em;
    margin-top: 14px;
  }
</style>
</head>
<body>
  <div class="card">
    <svg class="card-bands" viewBox="0 0 1200 710" aria-hidden="true">
      <defs>
        <linearGradient id="band-glow-top" x1="0" y1="0" x2="1" y2="0">
          <stop offset="0" stop-color="var(--band-blue)"/>
          <stop offset="1" stop-color="var(--band-steel)"/>
        </linearGradient>
        <linearGradient id="band-glow-bottom" x1="0" y1="0" x2="1" y2="0">
          <stop offset="0" stop-color="var(--band-mid)"/>
          <stop offset="1" stop-color="var(--band-blue)"/>
        </linearGradient>
      </defs>

      <!-- upper left bands -->
      <path d="M0 0 H370 L210 150 Q190 165 160 165 H0 Z" fill="url(#band-glow-top)" opacity="0.85"/>
      <path d="M0 205 H150 Q190 205 215 180 L410 0 H470 L250 210 Q215 245 170 245 H0 Z" fill="var(--band-blue)" opacity="0.55"/>
      <path d="M470 0 H640 L300 330 Q270 360 220 360 H0 V245 H170 Q215 245 250 210 Z" fill="var(--band-deep)" opacity="0.9"/>
      <path d="M700 0 H760 L420 330 H360 Z" fill="var(--band-mid)" opacity="0.45"/>

      <!-- right side broad band -->
      <path d="M880 0 H1200 V200 H1010 Q970 200 945 225 L650 520 H420 Z" fill="var(--band-deep)" opacity="0.8"/>

      <!-- lower right bands -->
      <path d="M1200 510 H870 Q830 510 805 535 L630 710 H1200 Z" fill="var(--band-mid)" opacity="0.8"/>
      <path d="M1200 560 H960 Q925 560 905 580 L775 710 H1200 Z" fill="url(#band-glow-bottom)" opacity="0.75"/>
      <path d="M1200 600 H1040 Q1015 600 1000 615 L905 710 H1200 Z" fill="var(--band-steel)" opacity="0.55"/>
    </svg>

    <div class="brand-lockup">
      <div class="brand-square"></div>
      <h1 class="brand-name">
        <span class="brand-primary">COBALT</span>
        <span class="brand-secondary">BUILD GROUP</span>
      </h1>
    </div>
  </div>
</body>
</html>
```